Venlow Vaults -responsive, bootstrap website design

Looking to build a responsive service website.

Logo and pictures have been provided.

PLEASE REVIEW ATTACHED DESIGN STYLE GUIDES & CLIENT CREATIVE BRIEF FOR OUR REQUIREMENT. THANK YOU AND GOOD LUCK!
Updates

Industry/Entity Type

Build

```html
<!DOCTYPE html>
<html lang="en">
<head>
<meta charset="utf-8">
<title>Venlow Vaults</title>
<link rel="stylesheet" href="https://fonts.googleapis.com/css2?family=Open+Sans:wght@400;600&family=Libre+Baskerville:wght@400;700&family=Questrial&family=Hind:wght@500;600&display=swap">
<style>
:root{
  --ink:#1a1a1a;
  --text:#333;
  --muted:#8a8a8a;
  --line:#e2e2e2;
  --nav:#000;
  --white:#fff;
  --band:#f4f4f4;
  --green:#6aa62c;
  --footer:#2b2b2b;
  --footer-text:#e6e6e6;
}
*{box-sizing:border-box;margin:0;padding:0}
html,body{width:963px;height:1200px;overflow:hidden;background:var(--white)}
body{position:relative;font-family:"Open Sans",sans-serif;color:var(--text)}
.abs{position:absolute}

/* header */
.util-links{left:588px;top:12px;font-size:11.5px;color:#555;word-spacing:1px}
.util-links span{margin:0 6px;color:#777}
.search{left:103px;top:102px;width:235px;height:29px;border:1px solid var(--line);border-radius:2px;display:flex;align-items:center;padding-left:8px;gap:7px;font-size:10px;font-style:italic;color:#666}
.brand{left:400px;top:40px;width:164px;text-align:center;font-family:"Libre Baskerville",serif;font-size:22px;font-weight:400;color:var(--ink);line-height:1.25}
.cart{left:748px;top:84px;display:flex;gap:9px;align-items:center}
.cart-label{font-size:12px;color:#888;line-height:1.1}
.cart-count{font-size:18px;color:#444;line-height:1.1}

/* nav */
.nav{left:0;top:146px;width:963px;height:43px;background:var(--nav)}
.nav a{position:absolute;top:0;height:43px;line-height:43px;transform:translateX(-50%);color:var(--white);text-decoration:none;font-family:"Libre Baskerville",serif;font-size:12px;font-weight:400;letter-spacing:.3px}
.nav i{position:absolute;top:0;width:1px;height:43px;background:#444}

/* hero */
.hero{left:0;top:189px;width:963px;height:383px;background:linear-gradient(180deg,#b9c6c4 0%,#8ea08a 14%,#6e8d3e 28%,#557a2b 55%,#4a6a25 75%,#8a7a3a 100%)}
.hero-title{left:0;top:130px;width:955px;text-align:center;font-family:"Hind",sans-serif;font-weight:600;font-size:31px;color:var(--white);letter-spacing:.5px}
.hero-sub{left:0;top:174px;width:940px;text-align:center;font-family:"Hind",sans-serif;font-weight:500;font-size:22px;color:var(--white)}
.dots{left:453px;top:362px;display:flex;gap:5px}
.dots b{width:10px;height:10px;border-radius:50%;background:var(--white)}

/* features */
.features{left:0;top:572px;width:963px;height:179px;background:linear-gradient(180deg,#fff 0%,var(--band) 100%);border-bottom:1px solid var(--line)}
.feature{position:absolute;top:38px;width:190px;transform:translateX(-50%);text-align:center}
.feature h3{font-family:"Questrial",sans-serif;font-weight:400;font-size:16px;color:var(--ink);line-height:18px;margin-bottom:3px}
.feature p{font-size:9.6px;color:#777;line-height:15px;height:32px}
.btn{display:inline-block;margin-top:10px;width:82px;height:25px;line-height:25px;background:var(--ink);color:var(--white);border-radius:3px;font-size:10px;font-weight:600}
.divider{position:absolute;top:0;width:1px;height:179px;background:var(--line)}

/* content */
.section-title{font-family:"Questrial",sans-serif;font-size:20px;color:#333;font-weight:400}
.gallery{left:95px;top:838px;display:grid;grid-template-columns:repeat(3,76px);gap:3px 4px}
.gallery div{height:59px}
.news-item{width:240px}
.news-item h4{font-size:11.5px;font-weight:600;color:#333;margin-bottom:4px}
.news-item p{font-size:9.5px;color:var(--muted);line-height:15px}
.blog-item{display:flex;gap:8px;width:240px}
.blog-thumb{width:64px;height:51px;flex:none}
.blog-item h4{font-family:"Questrial",sans-serif;font-size:12.5px;font-weight:400;color:var(--green);margin:2px 0 2px}
.blog-item p{font-size:9.5px;color:var(--muted);line-height:15px}

/* footer */
.footer{left:0;top:1092px;width:963px;height:108px;background:var(--footer)}
.footer-links{left:99px;top:25px;font-size:11.5px;font-weight:600;color:var(--footer-text)}
.footer-links span{margin:0 5px;font-weight:400}
.copyright{left:99px;top:50px;font-size:10px;color:#bbb}
.social{left:779px;top:25px;display:flex;gap:8px}
.social b{width:20px;height:20px;border-radius:2px;background:#5a6f9c}
.social b:nth-child(2){background:#49b3e6}
.social b:nth-child(3){background:#8a7665}
</style>
</head>
<body>

<header>
  <nav class="abs util-links">My Account<span>|</span>Shop Now<span>|</span>Contact Us<span>|</span>Wish List</nav>
  <div class="abs search">
    <svg width="15" height="15" viewBox="0 0 15 15"><circle cx="6" cy="6" r="5" fill="none" stroke="#aaa" stroke-width="1.6"/><line x1="9.8" y1="9.8" x2="14" y2="14" stroke="#aaa" stroke-width="1.8"/></svg>
    Search here..
  </div>
  <div class="abs brand">Venlow<br>Vaults</div>
  <div class="abs cart">
    <svg width="34" height="38" viewBox="0 0 34 38"><path d="M10 12V9a7 7 0 0 1 14 0v3" fill="none" stroke="#d4d4d4" stroke-width="3"/><rect x="2" y="12" width="30" height="24" rx="4" fill="#d4d4d4"/></svg>
    <div><div class="cart-label">My Cart</div><div class="cart-count">0 items</div></div>
  </div>
</header>

<nav class="abs nav">
  <a style="left:183px">HOME</a><i style="left:229px"></i>
  <a style="left:281px">ABOUT</a><i style="left:330px"></i>
  <a style="left:380px">WINES</a><i style="left:428px"></i>
  <a style="left:477px">STORE</a><i style="left:522px"></i>
  <a style="left:572px">NEWS</a><i style="left:614px"></i>
  <a style="left:726px">JOIN THE VENLOW FAMILY</a>
</nav>

<section class="abs hero" role="img" aria-label="Vineyard rows stretching across rolling green hills under a pale sky">
  <h1 class="abs hero-title">SUSPENDISSE VULPUTATE ALIQUAM</h1>
  <h2 class="abs hero-sub">LECTUS QUIS DUI VIVERRA VESTIBULUM</h2>
  <div class="abs dots"><b></b><b></b><b></b><b></b></div>
</section>

<section class="abs features">
  <i class="divider" style="left:284px"></i>
  <i class="divider" style="left:477px"></i>
  <i class="divider" style="left:672px"></i>
  <div class="feature" style="left:184px;top:38px">
    <h3>RETAIL / DEALER<br>LOCATOR</h3>
    <p>Mauris vel lacus vitae felis vestibu-<br>lum volutpat Etiam nunc</p>
    <span class="btn">Read More</span>
  </div>
  <div class="feature" style="left:380px">
    <h3>PURCHASE WINES</h3>
    <p style="height:50px">Nulla elementum dui ut augue<br>Aliquam vehicula mi at mauris<br>Maecenas placerat</p>
    <span class="btn" style="margin-top:0">Read More</span>
  </div>
  <div class="feature" style="left:575px">
    <h3>WHY CHOOSE US</h3>
    <p style="height:50px">Nulla elementum dui ut augue<br>Aliquam vehicula mi at mauris<br>Maecenas placerat</p>
    <span class="btn" style="margin-top:0">Read More</span>
  </div>
  <div class="feature" style="left:770px">
    <h3>STORE &amp; MEDIA</h3>
    <p style="height:50px">Nulla elementum dui ut augue<br>Aliquam vehicula mi at mauris<br>Maecenas placerat</p>
    <span class="btn" style="margin-top:0">Read More</span>
  </div>
</section>

<h2 class="abs section-title" style="left:95px;top:802px">Photo/Video Gallery</h2>
<div class="abs gallery">
  <div role="img" aria-label="Farmhouse among vineyards" style="background:linear-gradient(#8fc46a,#5e9a35)"></div>
  <div role="img" aria-label="Golden vineyard valley with mountains" style="background:linear-gradient(#8a8a7a,#c8a82a)"></div>
  <div role="img" aria-label="Vine rows on a slope" style="background:linear-gradient(#7fbf4a,#4f8a2a)"></div>
  <div role="img" aria-label="Terraced green vineyard" style="background:linear-gradient(#6aa83a,#3f7a22)"></div>
  <div role="img" aria-label="Vineyard hillside" style="background:linear-gradient(#8fb870,#5a8a3a)"></div>
  <div role="img" aria-label="Winding vineyard path" style="background:linear-gradient(#a0c870,#6a9a3a)"></div>
  <div role="img" aria-label="Wine glass with cheese and grapes" style="background:linear-gradient(#cfe09a,#8fb050)"></div>
  <div role="img" aria-label="Vineyard rows at midday" style="background:linear-gradient(#9ac060,#5a8a30)"></div>
  <div role="img" aria-label="Couple tasting red wine" style="background:linear-gradient(#b8a8a0,#8a5a50)"></div>
</div>

<h2 class="abs section-title" style="left:366px;top:802px">Latest News</h2>
<article class="abs news-item" style="left:367px;top:838px">
  <h4>Praesent sit amet est</h4>
  <p>dictum dolor eu dictum porttitor enim felis viverra mi eget luctus massa purus quis odio Etiam</p>
</article>
<article class="abs news-item" style="left:367px;top:904px">
  <h4>Vivamus porttitor purus</h4>
  <p>dictum dolor eu dictum porttitor enim felis viverra mi eget luctus massa purus quis odio Etiam</p>
</article>
<article class="abs news-item" style="left:367px;top:972px">
  <h4>Nullam enim leo egestas</h4>
  <p>dictum dolor eu dictum porttitor enim felis viverra mi eget luctus massa purus quis odio Etiam</p>
</article>

<h2 class="abs section-title" style="left:628px;top:802px">Recent Blog Post</h2>
<article class="abs blog-item" style="left:629px;top:839px">
  <div class="blog-thumb" role="img" aria-label="Autumn vineyard rows" style="background:linear-gradient(#9ab860,#a08040)"></div>
  <div><h4>Blog Post TItle</h4><p>Donec convallis pede venenatis nibh Duis quam Nam eget lacus</p></div>
</article>
<article class="abs blog-item" style="left:629px;top:908px">
  <div class="blog-thumb" role="img" aria-label="Vineyard valley under blue sky" style="background:linear-gradient(#8ab0c8,#6a9a40)"></div>
  <div><h4>Blog Post TItle</h4><p>Donec convallis pede venenatis nibh Duis quam Nam eget lacus</p></div>
</article>
<article class="abs blog-item" style="left:629px;top:977px">
  <div class="blog-thumb" role="img" aria-label="Farmhouse in green vineyard" style="background:linear-gradient(#a8c890,#5e9a35)"></div>
  <div><h4>Blog Post TItle</h4><p>Donec convallis pede venenatis nibh Duis quam Nam eget lacus</p></div>
</article>

<footer class="abs footer">
  <nav class="abs footer-links">Home<span>|</span>About Us<span>|</span>SERVICES<span>|</span>PROJECTS<span>|</span>NEWS<span>|</span>SUPPORT<span>|</span>CONTACT</nav>
  <p class="abs copyright">© 2013 Company Name.&nbsp; All right reserved.&nbsp; Term of Use</p>
  <div class="abs social" aria-label="Social links"><b></b><b></b><b></b></div>
</footer>

</body>
</html>
```